The maple crew

I want it as prefession and attractive as possible we are a lawnmowing business

Phone number 605-318-2264
Name- Carlos Whitfield
Email- themaplecrewsd@fernpost.com

```html
<!DOCTYPE html>
<html lang="en">
<head>
<meta charset="utf-8">
<title>The maple crew — Business Card</title>
<link href="https://fonts.googleapis.com/css2?family=Montserrat:wght@400;600;800&display=swap" rel="stylesheet">
<style>
  :root {
    --forest: #0b6139;
    --leaf: #5fbf45;
    --paper: #ffffff;
    --ink: #222222;
    --backdrop: #4a4a4a;
  }
  html, body {
    margin: 0;
    padding: 0;
    width: 1200px;
    height: 875px;
    overflow: hidden;
    background: var(--backdrop);
    font-family: "Montserrat", Arial, sans-serif;
  }
  .canvas {
    position: relative;
    width: 1200px;
    height: 875px;
  }
  .card {
    position: absolute;
    left: 280px;
    width: 640px;
    height: 366px;
    border-radius: 26px;
    box-sizing: border-box;
    box-shadow: 0 10px 24px rgba(0,0,0,0.35);
  }
  .card-front {
    top: 45px;
    background: var(--forest);
    display: flex;
    align-items: center;
    justify-content: center;
  }
  .card-back {
    top: 459px;
    background: var(--paper);
    border-bottom: 3px solid var(--forest);
    display: flex;
    flex-direction: column;
    align-items: center;
    padding-top: 58px;
  }
  .brand-name {
    font-weight: 800;
    text-transform: uppercase;
    letter-spacing: 1px;
    line-height: 1;
  }
  .card-front .brand-name {
    color: var(--paper);
    font-size: 56px;
  }
  .card-back .brand-name {
    color: var(--forest);
    font-size: 44px;
  }
  .person-name {
    margin-top: 40px;
    font-size: 30px;
    font-weight: 800;
  }
  .person-first { color: var(--leaf); }
  .person-last { color: var(--forest); }
  .contact-icons {
    display: flex;
    gap: 8px;
    margin-top: 14px;
  }
  .contact-icons svg { width: 24px; height: 24px; }
  .contact-line {
    margin-top: 12px;
    font-size: 18px;
    font-weight: 400;
    color: var(--ink);
    letter-spacing: 0.3px;
  }
</style>
</head>
<body>
<main class="canvas">
  <section class="card card-front" aria-label="Card front">
    <span class="brand-name">The maple crew</span>
  </section>

  <section class="card card-back" aria-label="Card back">
    <span class="brand-name">The maple crew</span>
    <div class="person-name">
      <span class="person-first">Carlos</span>
      <span class="person-last">Whitfield</span>
    </div>
    <div class="contact-icons">
      <svg viewBox="0 0 24 24" aria-label="Phone">
        <circle cx="12" cy="12" r="12" fill="var(--forest)"/>
        <path d="M8.2 6.5c.5-.4 1.2-.3 1.5.2l1.1 1.8c.3.5.2 1.1-.2 1.4l-.8.6c.6 1.3 1.5 2.3 2.7 2.9l.6-.8c.4-.4 1-.5 1.4-.2l1.8 1.1c.5.3.6 1 .2 1.5l-.8.9c-.6.6-1.5.8-2.3.5-3-1.2-5.2-3.5-6.3-6.4-.3-.8-.1-1.7.5-2.3z" fill="#fff"/>
      </svg>
      <svg viewBox="0 0 24 24" aria-label="Email">
        <circle cx="12" cy="12" r="12" fill="var(--leaf)"/>
        <rect x="6" y="8" width="12" height="8.5" rx="1" fill="#fff"/>
        <path d="M6.5 8.6 12 13l5.5-4.4" fill="none" stroke="var(--leaf)" stroke-width="1.2"/>
      </svg>
    </div>
    <div class="contact-line">605-318-2264</div>
    <div class="contact-line">themaplecrewsd@fernpost.com</div>
  </section>
</main>
</body>
</html>
```